The Cleaver Duchess great Quarterly Meat Deal

Hi I somehow need a flyer to promote this beef deal there is a box for each month, must sign up for 3 months and each month Box will be delivered to them buy 10th of the month. People can purchash 3 months at a time and can use easy split if they want.
price is $765per quarter pick up $840 south island delivered or $ 940 dollars North Island Delivered.
I guess it can look a bit like a poster maybe A3 to make it fit, it is high class Angus Beef, Free range North Canterbury Pork and Canterbury Lamb
This deal is over 35% cheaper than Shop Rite Max supermarket

Industry/Entity Type

Meat reatail

Requirements
Nice to have
• The 35% cheaper than supermarket is massive, and the quality is much better than anything at supermarket
Should not have
• Check out our website cleaverduchess.co.nz we also on friendnook

```html
<!DOCTYPE html>
<html lang="en">
<head>
<meta charset="utf-8">
<title>The Cleaver Duchess – Great Quarterly Meat Deal</title>
<link rel="stylesheet" href="https://fonts.googleapis.com/css2?family=Anton&family=Bebas+Neue&family=Poppins:wght@400;600;700;800&family=Roboto+Condensed:wght@400;700&display=swap">
<style>
:root{
  --stage:#cbcbcb;
  --ink:#0d0d0d;
  --wall:#1c1c1c;
  --red:#e8141b;
  --gold:#f0b30f;
  --white:#ffffff;
  --muted:#e6e6e6;
}
*{margin:0;padding:0;box-sizing:border-box}
html,body{width:1200px;height:2400px;overflow:hidden;background:var(--stage)}
.page{position:absolute;left:226px;width:747px;height:1056px;overflow:hidden;
  background:
    radial-gradient(ellipse 120px 160px at 170px 20px,rgba(255,255,255,.16),transparent 70%),
    radial-gradient(ellipse 120px 160px at 375px 10px,rgba(255,255,255,.14),transparent 70%),
    radial-gradient(ellipse 120px 160px at 600px 20px,rgba(255,255,255,.16),transparent 70%),
    linear-gradient(180deg,#202020 0%,var(--wall) 50%,#121212 100%);
  color:var(--white);font-family:"Poppins",sans-serif}
.flyer-front{top:107px}
.flyer-back{top:1218px}
.abs{position:absolute}

/* front */
.ribbon-art{left:0;top:0;width:165px;height:160px;
  background:radial-gradient(ellipse at 35% 35%,rgba(216,34,28,.85) 0%,rgba(150,16,16,.5) 45%,rgba(28,28,28,0) 75%)}
.headline{left:0;width:747px;text-align:center;font-family:"Anton",sans-serif;line-height:1}
.headline-top{top:62px;font-size:75px;color:var(--red);transform:rotate(-4deg);padding-left:18px}
.headline-main{top:136px;font-size:108px;color:var(--gold);padding-left:8px;transform:scaleY(1.2);transform-origin:top center}
.tagline{top:280px;left:0;width:747px;padding-left:8px;text-align:center;font-family:"Bebas Neue",sans-serif;font-size:34px;letter-spacing:3.5px}
.signup{left:50px;top:343px;font-weight:700}
.signup-lead{font-size:27px;line-height:1.1}
.signup-months{font-size:47px;color:var(--gold);font-weight:800;line-height:1}
.delivery{left:322px;top:346px;width:400px}
.delivery-lead{font-size:17.6px;font-weight:600;line-height:1.3}
.delivery-lead em{font-style:normal;color:var(--red)}
.delivery-note{font-size:11.8px;line-height:1.25;margin-top:2px;color:var(--muted)}
.badge{width:156px;height:156px;top:466px}
.badge svg{width:100%;height:100%;display:block}
.badge-label{position:absolute;inset:0;display:flex;align-items:center;justify-content:center;text-align:center;font-family:"Anton",sans-serif;font-size:26px;line-height:.95;color:var(--white);padding-top:6px}
.badge-label.solo{font-size:34px;padding-top:10px}
.price{width:90px;height:90px;top:436px}
.price svg{width:100%;height:100%;display:block}
.price-tag{position:absolute;inset:0;display:flex;flex-direction:column;align-items:center;justify-content:center;font-family:"Anton",sans-serif}
.price-amount{font-size:31px;color:var(--ink);line-height:1}
.price-unit{font-family:"Bebas Neue",sans-serif;font-size:10px;color:var(--white);letter-spacing:.5px}
.saving{left:67px;top:640px;font-family:"Poppins",sans-serif;font-weight:800;font-size:86px;color:var(--gold);line-height:1}
.saving sup{font-size:50px;vertical-align:top;position:relative;top:-6px}
.saving-box{left:221px;top:646px;width:472px;height:83px;border:1.5px solid var(--gold);padding:5px 0 0 9px;font-weight:600;font-size:20.8px;line-height:1.17;white-space:nowrap}
.meat-photo{left:0;top:745px;width:747px;height:262px;
  background:radial-gradient(ellipse 230px 80px at 120px 150px,#8a1e23,transparent 75%),
             radial-gradient(ellipse 200px 90px at 380px 180px,#a23a44,transparent 75%),
             radial-gradient(ellipse 230px 80px at 620px 160px,#b8566a,transparent 75%),
             linear-gradient(180deg,#161616,#262020 60%,#0d0d0d)}
.brand{left:0;width:747px;top:760px;text-align:center;font-family:"Anton",sans-serif;font-size:40px;color:var(--red);letter-spacing:1px}
.site{left:0;width:747px;text-align:center;font-weight:700;font-size:16px;letter-spacing:4px;top:1000px}

/* back */
.year-title{top:28px;left:0;width:747px;text-align:center;font-weight:800;font-size:38px;letter-spacing:5px;color:var(--gold)}
.month-card{position:absolute;width:211px;height:196px;border:3px solid var(--red);border-radius:6px;background:rgba(10,10,10,.55)}
.month-card.gold{border-color:var(--gold)}
.month-name{position:absolute;top:-3px;left:-3px;width:130px;height:17px;background:var(--red);color:var(--white);
  font-weight:700;font-size:11.5px;line-height:17px;padding-left:10px;clip-path:polygon(0 0,100% 0,88% 100%,0 100%)}
.gold .month-name{background:var(--gold);color:var(--ink)}
.month-total{position:absolute;bottom:-22px;right:-3px;width:78px;height:23px;background:var(--red);color:var(--white);
  font-weight:700;font-size:12.5px;line-height:23px;text-align:right;padding-right:10px;clip-path:polygon(14% 0,100% 0,100% 100%,0 100%)}
.gold .month-total{background:var(--gold);color:var(--ink)}
.month-items{list-style:none;position:absolute;top:20px;left:9px;right:12px;font-family:"Roboto Condensed",sans-serif;font-size:6.3px;line-height:8.7px;color:var(--white)}
.month-items li{display:flex;justify-content:space-between;white-space:nowrap}
.month-items b{font-weight:400;color:var(--gold);width:18px}
.c1{left:44px}.c2{left:268px}.c3{left:496px}
.r1{top:79px}.r2{top:308px}.r3{top:539px}.r4{top:767px}
</style>
</head>
<body>

<section class="page flyer-front">
  <div class="abs ribbon-art" role="img" aria-label="Red gift ribbon bow in the corner"></div>
  <h1>
    <span class="abs headline headline-top">GREAT QUARTERLY</span>
    <span class="abs headline headline-main">MEAT DEAL</span>
  </h1>
  <p class="abs tagline">THERE IS A BOX FOR EACH MONTH</p>

  <div class="abs signup">
    <p class="signup-lead">MUST SIGN UP FOR</p>
    <p class="signup-months">3 MONTHS</p>
  </div>
  <div class="abs delivery">
    <p class="delivery-lead">AND EACH MONTH BOX WILL BE<br>DELIVERED TO THEM BY <em>10TH OF THE MONTH</em></p>
    <p class="delivery-note">People can purchash 3 months at a time and can use<br>easy split if they want.</p>
  </div>

  <div class="abs badge" style="left:74px">
    <svg viewBox="-80 -80 160 160"><circle r="70" fill="#f0b30f" stroke="#f0b30f" stroke-width="9" stroke-dasharray="3.7 3.6"/><circle r="64" fill="#e8141b"/></svg>
    <div class="badge-label solo">PICK UP</div>
  </div>
  <div class="abs badge" style="left:298px">
    <svg viewBox="-80 -80 160 160"><circle r="70" fill="#f0b30f" stroke="#f0b30f" stroke-width="9" stroke-dasharray="3.7 3.6"/><circle r="64" fill="#e8141b"/></svg>
    <div class="badge-label">SOUTH<br>ISLAND<br>DELIVERED</div>
  </div>
  <div class="abs badge" style="left:510px">
    <svg viewBox="-80 -80 160 160"><circle r="70" fill="#f0b30f" stroke="#f0b30f" stroke-width="9" stroke-dasharray="3.7 3.6"/><circle r="64" fill="#e8141b"/></svg>
    <div class="badge-label">NORTH<br>ISLAND<br>DELIVERED</div>
  </div>

  <div class="abs price" style="left:165px">
    <svg viewBox="-50 -50 100 100"><circle r="42" fill="#f0b30f" stroke="#f0b30f" stroke-width="7" stroke-dasharray="3 3"/><circle r="38" fill="#f0b30f" stroke="#e8141b" stroke-width="1"/></svg>
    <div class="price-tag"><span class="price-amount">$765</span><span class="price-unit">PER QUARTER</span></div>
  </div>
  <div class="abs price" style="left:390px">
    <svg viewBox="-50 -50 100 100"><circle r="42" fill="#f0b30f" stroke="#f0b30f" stroke-width="7" stroke-dasharray="3 3"/><circle r="38" fill="#f0b30f" stroke="#e8141b" stroke-width="1"/></svg>
    <div class="price-tag"><span class="price-amount">$840</span><span class="price-unit">PER QUARTER</span></div>
  </div>
  <div class="abs price" style="left:610px">
    <svg viewBox="-50 -50 100 100"><circle r="42" fill="#f0b30f" stroke="#f0b30f" stroke-width="7" stroke-dasharray="3 3"/><circle r="38" fill="#f0b30f" stroke="#e8141b" stroke-width="1"/></svg>
    <div class="price-tag"><span class="price-amount">$940</span><span class="price-unit">PER QUARTER</span></div>
  </div>

  <p class="abs saving">35<sup>%</sup></p>
  <p class="abs saving-box">CHEAPER THAN SUPERMARKET IS MASSIVE,<br>AND THE QUALITY IS MUCH BETTER THAN<br>ANYTHING AT SUPERMARKET</p>

  <div class="abs meat-photo" role="img" aria-label="Raw beef steaks, a tomahawk cut and sliced pork on a wooden board with cherry tomatoes and herbs"></div>
  <p class="abs brand">The Cleaver Duchess</p>
  <p class="abs site">www.cleaverduchess.co.nz</p>
</section>

<section class="page flyer-back">
  <h2 class="abs year-title">YEARLY OFFEREING</h2>

  <article class="month-card c1 r1"><h3 class="month-name">JANUARY</h3><ul class="month-items">
    <li><span>Ribeye 2x 500g packs</span><b>1</b></li><li><span>stir fry 500g</span><b>0.5</b></li><li><span>Corned beef 1.5 kg</span><b>1.5</b></li><li><span>Bier stix5stix per pack x2 packs</span><b>0.3</b></li><li><span>schnitzel 500g packs x2</span><b>1</b></li><li><span>Mince 500g Tubex2</span><b>1</b></li><li><span>Herb and garlic 500g x 2 Packs</span><b>1</b></li><li><span>Irish pork Sausage 500 x 2 packs</span><b>1</b></li><li><span>Lamb Mint Sausages 2x500g</span><b>1</b></li><li><span>Cross cut BBQ steak 4 steaks x2 packs 500g</span><b>1</b></li><li><span>Family/M/Pie</span><b>2</b></li><li><span>Saveloys 6 sausages 2xpacks</span><b>1</b></li><li><span>Diced pork 500g</span><b>0.5</b></li><li><span>Loin Chops 500g pack</span><b>0.5</b></li><li><span>Pork Mince 500g pack</span><b>0.5</b></li><li><span>Rolled shoulder 2kg</span><b>2</b></li><li><span>Lamb loin chops 600g</span><b>0.6</b></li><li><span>Rump steak 2x600g</span><b>1.2</b></li>
  </ul><p class="month-total">17.6</p></article>

  <article class="month-card gold c2 r1"><h3 class="month-name">FEBRUARY</h3><ul class="month-items">
    <li><span>Sirloin Stk 2x 600g</span><b>1.2</b></li><li><span>schnitzel 500g packs x2</span><b>1</b></li><li><span>Pork Stirfry 2x 500g</span><b>1</b></li><li><span>Streaky Bacon 300g x 3packs</span><b>0.9</b></li><li><span>Traditional Hand crafted Sliced ham 2x400g packs</span><b>0.8</b></li><li><span>Diced lamb 500g</span><b>0.5</b></li><li><span>Diced pork 500g</span><b>0.5</b></li><li><span>Small/M/Pie</span><b>1</b></li><li><span>Small/MC/Pie</span><b>1</b></li><li><span>Mince 2x 500g Tube</span><b>1</b></li><li><span>Patties 6 patties 600g x2 packs</span><b>1.2</b></li><li><span>Beef Sausages 500g x2packs</span><b>1</b></li><li><span>Point end 2kg</span><b>2</b></li><li><span>Eye Fillet 1 pack 3 steaks</span><b>0.6</b></li><li><span>Bier stix5stix per pack x2 packs</span><b>0.3</b></li><li><span>Lamb Mint Sausages 2x500g</span><b>1</b></li><li><span>Saveloys 6 sausages 2xpacks</span><b>1</b></li><li><span>Cross cut BBQ steak 4 steaks x2 packs 500g</span><b>1</b></li>
  </ul><p class="month-total">17</p></article>

  <article class="month-card c3 r1"><h3 class="month-name">MARCH</h3><ul class="month-items">
    <li><span>Diced 600g</span><b>0.6</b></li><li><span>Ribeye 2x 500g packs</span><b>1</b></li><li><span>stir fry 500g</span><b>0.5</b></li><li><span>Bier stix5stix per pack x2 packs</span><b>0.3</b></li><li><span>Cross cut BBQ steak 4 steaks x2 packs 500g</span><b>1</b></li><li><span>Beef Bacon 400g</span><b>0.4</b></li><li><span>Cooked sliced silverside 400g x2packs</span><b>0.8</b></li><li><span>Herb and garlic 500g x 2 Packs</span><b>1</b></li><li><span>Beef Sausages 500g x2packs</span><b>1</b></li><li><span>Patties 6 patties 600g x2 packs</span><b>1.2</b></li><li><span>Mince 3x 500g Tube</span><b>1.5</b></li><li><span>Family/MC/Pie</span><b>2</b></li><li><span>Eye Fillet 1 pack 3 steaks</span><b>0.6</b></li><li><span>Sirloin Stk 2xpacks 600g</span><b>1.2</b></li><li><span>Pork Loin Chops 500g pack</span><b>0.5</b></li><li><span>Diced pork 500g</span><b>0.5</b></li><li><span>Pork Mince 500g pack</span><b>0.5</b></li><li><span>half leg lamb 1kg min</span><b>1</b></li><li><span>Irish pork Sausage 500 x 2 packs</span><b>1</b></li>
  </ul><p class="month-total">16.6</p></article>

  <article class="month-card gold c1 r2"><h3 class="month-name">APRIL</h3><ul class="month-items">
    <li><span>Herb and garlic 500g x 2 Packs</span><b>1</b></li><li><span>Irish pork Sausage 500 x 2 packs</span><b>1</b></li><li><span>Lamb Mint Sausages 2x500g</span><b>1</b></li><li><span>Sliced Mutton Ham 400g x2</span><b>3</b></li><li><span>Saveloys 6 sausages 2xpacks</span><b>1</b></li><li><span>Cross cut BBQ steak 4 steaks x2 packs 500g</span><b>1</b></li><li><span>Pork Mince 500g pack</span><b>0.5</b></li><li><span>Diced pork 500g</span><b>0.5</b></li><li><span>Corned beef 1.5 kg</span><b>1.5</b></li><li><span>Bier stix5stix per pack x2 packs</span><b>0.3</b></li><li><span>stir fry 500g</span><b>0.5</b></li><li><span>Mince 3 500g Tube</span><b>1.5</b></li><li><span>Patties 6 patties 600g x2 packs</span><b>1.2</b></li><li><span>Ribeye 2x 500g packs</span><b>1</b></li><li><span>Rump steak 2x600g</span><b>1.2</b></li><li><span>Diced pork 500g</span><b>0.5</b></li>
  </ul><p class="month-total">16.7</p></article>

  <article class="month-card c2 r2"><h3 class="month-name">MAY</h3><ul class="month-items">
    <li><span>Rolled Lamb Shoulder 1.5kg min</span><b>2</b></li><li><span>Diced skirt 600g</span><b>0.6</b></li><li><span>Gravy Beef 500g</span><b>0.5</b></li><li><span>Pot Roast 2</span><b>2</b></li><li><span>Pastrami 400g x2 packs</span><b>0.8</b></li><li><span>Beef Sausages 500g x2packs</span><b>1</b></li><li><span>Saveloys 6 sausages 2xpacks</span><b>1</b></li><li><span>Mince 500g Tubex2</span><b>1</b></li><li><span>Small/M/Pie</span><b>1</b></li><li><span>Small/MC/Pie</span><b>1</b></li><li><span>Sliced Mutton Ham 400g x2</span><b>0.9</b></li><li><span>Lamb loin chops 600g</span><b>0.6</b></li><li><span>Pork Stirfry 500g</span><b>0.5</b></li><li><span>Bacon hocks 1 Manuka smoked</span><b>0.5</b></li><li><span>Pork Stirfry 500g</span><b>0.5</b></li><li><span>Stewing Chuck steak 600g</span><b>0.6</b></li><li><span>Rolled Rib roast</span><b>1.5</b></li><li><span>Eye Fillet 1 pack 3 steaks</span><b>0.6</b></li><li><span>Diced lamb 500g</span><b>0.5</b></li>
  </ul><p class="month-total">17.1</p></article>

  <article class="month-card gold c3 r2"><h3 class="month-name">JUNE</h3><ul class="month-items">
    <li><span>Pot Roast 2</span><b>2</b></li><li><span>Point end 2kg</span><b>2</b></li><li><span>Beef Bacon 400g</span><b>0.4</b></li><li><span>Gravy Beef 500g</span><b>0.5</b></li><li><span>Traditional Hand crafted Sliced ham 2x400g packs</span><b>0.8</b></li><li><span>Rump steak 2x600g</span><b>1.2</b></li><li><span>Sirloin Stk 2xpacks 600g</span><b>1.2</b></li><li><span>Pork Loin Chops 500g pack</span><b>0.5</b></li><li><span>Mince 500g Tube x 4 packs</span><b>2</b></li><li><span>Herb and garlic 500g x 2 Packs</span><b>1</b></li><li><span>Family/MC/Pie</span><b>2</b></li><li><span>Rolled Lamb Shoulder 1.5kg min</span><b>2</b></li><li><span>Rolled Lamb Shoulder 1.5kg min</span><b>2</b></li><li><span>Diced chuck x 2 500g</span><b>1</b></li>
  </ul><p class="month-total">18.6</p></article>

  <article class="month-card c1 r3"><h3 class="month-name">JULY</h3><ul class="month-items">
    <li><span>Ribeye 2x 500g packs</span><b>1</b></li><li><span>Mince 3 500g Tube</span><b>1.5</b></li><li><span>Rump steak 2x600g</span><b>1.2</b></li><li><span>Pot Roast 2</span><b>2</b></li><li><span>Rolled Rib roast</span><b>1.5</b></li><li><span>Streaky Bacon 300g x 3packs</span><b>0.9</b></li><li><span>Sliced Mutton Ham 400g x2</span><b>0.8</b></li><li><span>Corned beef 1.5 kg</span><b>1.5</b></li><li><span>Pastrami 400g x2 packs</span><b>0.8</b></li><li><span>Lamb Mint Sausages 2x500g</span><b>1</b></li><li><span>Diced pork 500g</span><b>0.5</b></li><li><span>schnitzel 500g packs x2</span><b>1</b></li><li><span>Saveloys 6 sausages 2xpacks</span><b>1</b></li><li><span>Rump steak 2x600g</span><b>1.2</b></li><li><span>Beef Sausages 500g x2packs</span><b>1</b></li><li><span>Family/M/Pie</span><b>2</b></li>
  </ul><p class="month-total">18.9</p></article>

  <article class="month-card gold c2 r3"><h3 class="month-name">AUGUST</h3><ul class="month-items">
    <li><span>Diced skirt 600g</span><b>0.6</b></li><li><span>Pot Roast 2</span><b>2</b></li><li><span>Rolled Rib roast</span><b>1.5</b></li><li><span>Corned beef 1.5 kg</span><b>1.5</b></li><li><span>Bacon hocks 1 Manuka smoked</span><b>0.5</b></li><li><span>Diced chuck x 2 500g</span><b>1</b></li><li><span>Herb and garlic 500g x 2 Packs</span><b>1</b></li><li><span>Pork Stirfry 500g</span><b>0.5</b></li><li><span>Pork Loin Chops 500g pack</span><b>0.5</b></li><li><span>Traditional Hand crafted Sliced ham 2x400g packs</span><b>0.8</b></li><li><span>Diced pork 500g</span><b>0.5</b></li><li><span>schnitzel 500g packs x2</span><b>1</b></li><li><span>Eye Fillet 1 pack 3 steaks</span><b>0.6</b></li><li><span>Sirloin Stk 2xpacks 600g</span><b>1.2</b></li><li><span>Irish pork Sausage 500 x 2 packs</span><b>1</b></li><li><span>half leg lamb 1kg min</span><b>1</b></li><li><span>Sliced Mutton Ham 400g x2</span><b>0.8</b></li><li><span>Family/MC/Pie</span><b>2</b></li>
  </ul><p class="month-total">18</p></article>

  <article class="month-card c3 r3"><h3 class="month-name">SEPTEMBER</h3><ul class="month-items">
    <li><span>Small/M/Pie</span><b>1</b></li><li><span>Small/MC/Pie</span><b>1</b></li><li><span>Sirloin Stk 2x 600g</span><b>1.2</b></li><li><span>Eye Fillet 1 pack 3 steaks</span><b>0.6</b></li><li><span>Diced chuck x 2 500g</span><b>1</b></li><li><span>Point end 2kg</span><b>2</b></li><li><span>Beef Bacon 400g</span><b>0.4</b></li><li><span>Gravy Beef 500g</span><b>0.5</b></li><li><span>Family/MC/Pie</span><b>2</b></li><li><span>Saveloys 6 sausages 2xpacks</span><b>1</b></li><li><span>Lamb Mint Sausages 2x500g</span><b>1</b></li><li><span>Diced pork 500g</span><b>0.5</b></li><li><span>Lamb loin chops 600g</span><b>0.6</b></li><li><span>Mince 3 500g Tube</span><b>1.5</b></li><li><span>Bier stix5stix per pack x2 packs</span><b>0.3</b></li><li><span>Irish pork Sausage 500 x 2 packs</span><b>1</b></li><li><span>Beef Sausages 500g x2packs</span><b>1</b></li>
  </ul><p class="month-total">16.6</p></article>

  <article class="month-card gold c1 r4"><h3 class="month-name">OCTOBER</h3><ul class="month-items">
    <li><span>Ribeye 2x 500g packs</span><b>1</b></li><li><span>Saveloys 6 sausages 2xpacks</span><b>1</b></li><li><span>Beef Sausages 500g x2packs</span><b>1</b></li><li><span>Beef stir fry 500g</span><b>0.5</b></li><li><span>Cross cut BBQ steak 4 steaks x2 packs 500g</span><b>1</b></li><li><span>Pork Stirfry 500g</span><b>0.5</b></li><li><span>Streaky Bacon 300g x 3packs</span><b>0.9</b></li><li><span>Pastrami 400g x2 packs</span><b>0.8</b></li><li><span>Pork Loin Chops 500g pack</span><b>0.5</b></li><li><span>Pork Mince 2x 500g pack</span><b>1</b></li><li><span>Mince 3 500g Tube</span><b>1.5</b></li><li><span>Lamb Mint Sausages 2x500g</span><b>1</b></li><li><span>Irish pork Sausage 500 x 2 packs</span><b>1</b></li><li><span>Traditional Hand crafted Sliced ham 2x400g packs</span><b>0.8</b></li><li><span>Rump steak 2x600g</span><b>1.2</b></li><li><span>schnitzel 500g packs x2</span><b>1</b></li><li><span>Bier stix5stix per pack x2 packs</span><b>0.3</b></li><li><span>Patties 6 patties 600g x2 packs</span><b>1.2</b></li>
  </ul><p class="month-total">16.2</p></article>

  <article class="month-card c2 r4"><h3 class="month-name">NOVEMBER</h3><ul class="month-items">
    <li><span>Sirloin Stk 2xpacks 600g</span><b>1</b></li><li><span>Ribeye 2x 500g packs</span><b>1</b></li><li><span>Eye Fillet 1 pack 3 steaks</span><b>0.6</b></li><li><span>Beef Bacon 400g</span><b>0.4</b></li><li><span>Cross cut BBQ steak 4 steaks x2 packs 500g</span><b>1</b></li><li><span>Rump steak 2x600g</span><b>1.2</b></li><li><span>schnitzel 500g packs x2</span><b>1</b></li><li><span>Bier stix5stix per pack x2 packs</span><b>0.3</b></li><li><span>Patties 6 patties 600g x2 packs</span><b>1.2</b></li><li><span>Bier stix5stix per pack x2 packs</span><b>0.3</b></li><li><span>Irish pork Sausage 500 x 2 packs</span><b>1</b></li><li><span>Beef Sausages 500g x2packs</span><b>1</b></li><li><span>Traditional Hand crafted Sliced ham 2x400g packs</span><b>0.8</b></li><li><span>Mince 3 500g Tube</span><b>1.5</b></li><li><span>Pastrami 400g x2 packs</span><b>0.8</b></li><li><span>Herb and garlic 500g x 2 Packs</span><b>1</b></li><li><span>Mince 3 500g Tube</span><b>1.5</b></li><li><span>Pork Stirfry 500g</span><b>0.5</b></li>
  </ul><p class="month-total">16.3</p></article>

  <article class="month-card gold c3 r4"><h3 class="month-name">DECEMBER</h3><ul class="month-items">
    <li><span>Sirloin Stk 2xpacks 600g</span><b>1.2</b></li><li><span>Ribeye 2x 500g packs</span><b>1</b></li><li><span>Eye Fillet 1 pack 3 steaks</span><b>0.6</b></li><li><span>Patties 6 patties 600g x2 packs</span><b>1.2</b></li><li><span>schnitzel 500g packs x2</span><b>1</b></li><li><span>Bier stix5stix per pack x2 packs</span><b>0.3</b></li><li><span>Irish pork Sausage 500 x 2 packs</span><b>1</b></li><li><span>Beef Sausages 500g x2packs</span><b>1</b></li><li><span>Traditional Hand crafted Sliced ham 2x400g packs</span><b>0.8</b></li><li><span>Mince 3 500g Tube</span><b>1.5</b></li><li><span>Pastrami 400g x2 packs</span><b>0.8</b></li><li><span>Irish pork Sausage 500 x 2 packs</span><b>1</b></li><li><span>Beef Sausages 500g x2packs</span><b>1</b></li><li><span>Lamb Mint Sausages 2x500g</span><b>1</b></li><li><span>Herb and garlic 500g x 2 Packs</span><b>1</b></li><li><span>Mince 3 500g Tube</span><b>1.5</b></li><li><span>Pork Stirfry 500g</span><b>0.5</b></li>
  </ul><p class="month-total">15.9</p></article>

  <p class="abs site">www.cleaverduchess.co.nz</p>
</section>

</body>
</html>
```